Working Capital graphics

Our business advisory firm requires 9 images to be re-created and improved in the branding of our business.

The 9 images have been uploaded below and the colours and branding of the business can be found at the website www.thornwickadvisory.com.au

```html
<!DOCTYPE html>
<html lang="en">
<head>
<meta charset="utf-8">
<title>Receivables Drivers</title>
<link href="https://fonts.googleapis.com/css2?family=League+Spartan:wght@500;600;700&display=swap" rel="stylesheet">
<style>
  :root {
    --navy: #1b3a87;
    --cyan: #0cb2f2;
    --orange: #fb9526;
    --frame: #d4d4d4;
    --paper: #ffffff;
  }
  html, body {
    margin: 0;
    padding: 0;
    width: 1200px;
    height: 728px;
    overflow: hidden;
    background: var(--frame);
  }
  .canvas { display: block; width: 1200px; height: 728px; }
  .sheet { fill: var(--paper); }
  text { font-family: "League Spartan", "Jost", sans-serif; }
  .title { fill: var(--navy); font-size: 37px; font-weight: 700; letter-spacing: 0.5px; }
  .column-head { fill: var(--navy); font-size: 17.5px; font-weight: 600; text-anchor: middle; }
  .hub-ring { fill: none; stroke: var(--navy); stroke-width: 2.2; }
  .hub-fill { fill: var(--cyan); }
  .hub-label { fill: #fff; font-size: 24px; font-weight: 700; text-anchor: middle; }
  .link { fill: none; stroke: var(--navy); stroke-width: 1.6; }
  .process-pill { fill: var(--orange); }
  .process-label { fill: #fff; font-size: 17px; font-weight: 600; text-anchor: middle; letter-spacing: 0.3px; }
  .driver-bar, .subdriver-bar { fill: var(--cyan); }
  .bar-label { fill: #fff; font-size: 13.5px; font-weight: 600; text-anchor: middle; letter-spacing: 0.8px; }
  .step-ring { fill: var(--paper); stroke: var(--orange); stroke-width: 1.6; }
  .step-number { fill: var(--navy); font-size: 24px; font-weight: 700; text-anchor: middle; }
</style>
</head>
<body>
<svg class="canvas" viewBox="0 0 1200 728" xmlns="http://www.w3.org/2000/svg">
  <rect class="sheet" x="7" y="7" width="1186" height="713"/>

  <!-- headings -->
  <text class="title" x="66" y="90">RECEIVABLES</text>
  <text class="column-head" x="422" y="81">SUB-PROCESS</text>
  <text class="column-head" x="693" y="81">DRIVERS</text>
  <text class="column-head" x="1002" y="158">SUB-DRIVERS</text>

  <!-- hub -->
  <g class="hub">
    <circle class="hub-ring" cx="173" cy="352" r="106"/>
    <circle class="hub-fill" cx="173" cy="352" r="96"/>
    <text class="hub-label" x="173" y="347">RECEIVABLES</text>
    <text class="hub-label" x="173" y="370">DRIVERS</text>
  </g>

  <!-- connectors -->
  <g class="links">
    <path class="link" d="M331 159 V544 M331 159 H351 M331 338 H351 M331 544 H351"/>
    <path class="link" d="M518 159 H538 M538 114 V204 M538 114 H562 M538 158 H562 M538 204 H562"/>
    <path class="link" d="M518 338 H538 M538 303 V393 M538 303 H562 M538 347 H562 M538 393 H562"/>
    <path class="link" d="M518 544 H538 M538 514 V604 M538 514 H562 M538 559 H562 M538 604 H562"/>
    <path class="link" d="M826 348 H854 V193 H882"/>
    <path class="link" d="M826 393 H882 M854 358 V428 M854 358 H882 M854 428 H882"/>
    <path class="link" d="M882 476 H853 V545 H882"/>
    <path class="link" d="M826 561 H853 V655 H882 M853 588 H882 M853 621 H882"/>
  </g>

  <!-- sub-processes -->
  <g class="processes">
    <rect class="process-pill" x="351" y="139" width="167" height="40" rx="20"/>
    <text class="process-label" x="435" y="165">APPROVAL</text>
    <rect class="process-pill" x="351" y="318" width="167" height="40" rx="20"/>
    <text class="process-label" x="435" y="344">SALES</text>
    <rect class="process-pill" x="351" y="523" width="167" height="40" rx="20"/>
    <text class="process-label" x="435" y="549">COLLECTIONS</text>
  </g>

  <!-- drivers -->
  <g class="drivers">
    <path class="driver-bar" d="M603 100.5 H812.5 a13.5 13.5 0 0 1 0 27 H603 Z"/>
    <text class="bar-label" x="707" y="119">DIFFERNTIATED TERMS</text>
    <path class="driver-bar" d="M603 144.5 H812.5 a13.5 13.5 0 0 1 0 27 H603 Z"/>
    <text class="bar-label" x="707" y="163">COSTUMER AGREEMENTS</text>
    <path class="driver-bar" d="M603 190.5 H812.5 a13.5 13.5 0 0 1 0 27 H603 Z"/>
    <text class="bar-label" x="707" y="209">ACCOUNT SET-UP</text>
    <path class="driver-bar" d="M603 289.5 H812.5 a13.5 13.5 0 0 1 0 27 H603 Z"/>
    <text class="bar-label" x="707" y="308">RECEIPT PROCESS</text>
    <path class="driver-bar" d="M603 333.5 H812.5 a13.5 13.5 0 0 1 0 27 H603 Z"/>
    <text class="bar-label" x="707" y="352">TIME TO INVOICE</text>
    <path class="driver-bar" d="M603 379.5 H812.5 a13.5 13.5 0 0 1 0 27 H603 Z"/>
    <text class="bar-label" x="708" y="398" textLength="206" lengthAdjust="spacingAndGlyphs">COSTUMER PAYMENT BEHAVIOUR</text>
    <rect class="driver-bar" x="603" y="500.5" width="223" height="27"/>
    <text class="bar-label" x="707" y="519">PAYMENT CYCLE</text>
    <rect class="driver-bar" x="603" y="545.5" width="223" height="27"/>
    <text class="bar-label" x="707" y="564">COLLECTIONS</text>
    <rect class="driver-bar" x="603" y="590.5" width="223" height="27"/>
    <text class="bar-label" x="707" y="609">PENALTIES</text>
  </g>

  <!-- step numbers -->
  <g class="steps">
    <circle class="step-ring" cx="580" cy="114" r="18.5"/><text class="step-number" x="580" y="122">1</text>
    <circle class="step-ring" cx="580" cy="158" r="18.5"/><text class="step-number" x="580" y="166">2</text>
    <circle class="step-ring" cx="580" cy="204" r="18.5"/><text class="step-number" x="580" y="212">3</text>
    <circle class="step-ring" cx="580" cy="303" r="18.5"/><text class="step-number" x="580" y="311">4</text>
    <circle class="step-ring" cx="580" cy="347" r="18.5"/><text class="step-number" x="580" y="355">5</text>
    <circle class="step-ring" cx="580" cy="393" r="18.5"/><text class="step-number" x="580" y="401">6</text>
    <circle class="step-ring" cx="580" cy="514" r="18.5"/><text class="step-number" x="580" y="522">7</text>
    <circle class="step-ring" cx="580" cy="559" r="18.5"/><text class="step-number" x="580" y="567">8</text>
    <circle class="step-ring" cx="580" cy="604" r="18.5"/><text class="step-number" x="580" y="612">9</text>
  </g>

  <!-- sub-drivers -->
  <g class="subdrivers">
    <rect class="subdriver-bar" x="882" y="179.5" width="251" height="27" rx="13.5"/><text class="bar-label" x="1007" y="198">CASH</text>
    <rect class="subdriver-bar" x="882" y="215.5" width="251" height="27" rx="13.5"/><text class="bar-label" x="1007" y="234">BANKING PROCESS</text>
    <rect class="subdriver-bar" x="882" y="267.5" width="251" height="27" rx="13.5"/><text class="bar-label" x="1007" y="286">SALES DELIVERY</text>
    <rect class="subdriver-bar" x="882" y="301.5" width="251" height="27" rx="13.5"/><text class="bar-label" x="1007" y="320">INVOICING</text>
    <rect class="subdriver-bar" x="882" y="344.5" width="251" height="27" rx="13.5"/><text class="bar-label" x="1007" y="363">KPI</text>
    <rect class="subdriver-bar" x="882" y="379.5" width="251" height="27" rx="13.5"/><text class="bar-label" x="1007" y="398">RELATIONSHIP</text>
    <rect class="subdriver-bar" x="882" y="413.5" width="251" height="27" rx="13.5"/><text class="bar-label" x="1007" y="432">PRICING</text>
    <rect class="subdriver-bar" x="882" y="462.5" width="251" height="27" rx="13.5"/><text class="bar-label" x="1007" y="481">CLOSING DATE</text>
    <rect class="subdriver-bar" x="882" y="496.5" width="251" height="27" rx="13.5"/><text class="bar-label" x="1007" y="515">TIME TO PROCESS</text>
    <rect class="subdriver-bar" x="882" y="531.5" width="251" height="27" rx="13.5"/><text class="bar-label" x="1007" y="550">INVOICING CYCLE</text>
    <rect class="subdriver-bar" x="882" y="574.5" width="251" height="27" rx="13.5"/><text class="bar-label" x="1007" y="593">TRACKING</text>
    <rect class="subdriver-bar" x="882" y="607.5" width="251" height="27" rx="13.5"/><text class="bar-label" x="1007" y="626">METHODS</text>
    <rect class="subdriver-bar" x="882" y="641.5" width="251" height="27" rx="13.5"/><text class="bar-label" x="1007" y="660">AGENCIES</text>
  </g>
</svg>
</body>
</html>
```